TKVB Business card

HI there we're looking for a business card design. We don't know exactly what we'd want, so anything from classy, to retro is great with us. just would like something that is bold but not too busy. And definitely stand out. you can Incorporate our colors as in our logo, and the TKVB and TkvbDecorativeConcrete in our logo can be seperate they do not have to be together. Thanks for your time.

we'd require 3 names, each on separate cards
C/O Howard Pilcher 780-555-0142
C/O Luc-Andre Fontaine 780-555-0187
C/O Denis Ouellet 780-555-0163

would like the Facebook 'F' insignia with our Facebook page
TkvbDecorativeConcrete or www.facebook.com/TkvbDecorativeConcrete
Our website
www.TkvbLtd.ca

Our Emails.
Howard@TkvbLtd.ca, Luc-Andre@TkvbLtd.ca, Denis@TkvbLtd.ca

Address
24517-63st NW, Cedarvale Northland, T6W-2K8

Reason: Being extended because I have been in the hospital the past few days and in havnt been able to provide enough feedback to the designers.

```html
<!DOCTYPE html>
<html lang="en">
<head>
<meta charset="utf-8">
<title>TKVB Decorative Concrete – Business Card</title>
<link rel="stylesheet" href="https://fonts.googleapis.com/css2?family=Open+Sans:wght@400;600;700&display=swap">
<style>
  :root {
    --bg: #e6e4e1;
    --card-white: #ffffff;
    --card-dark: #3d3d40;
    --mark-dark: #2f2f32;
    --ink: #3a3a3c;
    --ink-soft: #555558;
    --orange: #f26a1b;
    --orange-deep: #e25a12;
  }
  * { box-sizing: border-box; margin: 0; padding: 0; }
  html, body { width: 1200px; height: 800px; overflow: hidden; }
  body {
    background: var(--bg);
    font-family: "Open Sans", Arial, sans-serif;
    color: var(--ink);
    position: relative;
  }

  /* Back of card */
  .card-back {
    position: absolute;
    left: 90px; top: 100px;
    width: 340px; height: 600px;
    background: var(--card-dark);
    border-radius: 4px;
    box-shadow: 0 8px 24px rgba(0,0,0,.18);
    overflow: hidden;
  }
  .card-back .back-name {
    position: absolute;
    left: 50%; top: 50%;
    transform: translate(-50%, -50%) rotate(90deg);
    font-weight: 700;
    font-size: 190px;
    letter-spacing: 6px;
    color: var(--mark-dark);
    line-height: 1;
  }

  /* Front of card */
  .card-front {
    position: absolute;
    left: 520px; top: 228px;
    width: 600px; height: 343px;
    background: var(--card-white);
    border-radius: 4px;
    box-shadow: 0 8px 24px rgba(0,0,0,.18);
    overflow: hidden;
  }
  .brand {
    position: absolute;
    left: 34px; top: 30px;
    display: flex; align-items: center;
  }
  .brand-square {
    width: 46px; height: 46px;
    background: var(--orange);
    margin-right: 14px;
  }
  .brand-name {
    font-weight: 700;
    font-size: 48px;
    letter-spacing: 3px;
    color: var(--ink);
    line-height: 1;
  }
  .brand-divider {
    width: 1px; height: 52px;
    background: var(--orange);
    margin: 0 16px;
  }
  .brand-tagline {
    font-size: 15px;
    letter-spacing: 1px;
    text-transform: uppercase;
    color: var(--ink);
    line-height: 1.25;
  }

  .person-name {
    position: absolute;
    left: 34px; top: 118px;
    font-weight: 700;
    font-size: 17px;
    letter-spacing: .5px;
    text-transform: uppercase;
  }
  .person-name .first { color: var(--orange); }
  .person-name .last { color: var(--ink-soft); }

  .contact {
    position: absolute;
    left: 300px; top: 200px;
    font-size: 13.5px;
    color: var(--ink);
    line-height: 1.45;
  }
  .contact .address { margin-bottom: 6px; }
  .contact-row { display: flex; align-items: center; gap: 8px; }
  .contact-icon {
    width: 13px; height: 13px;
    background: var(--orange);
    border-radius: 2px;
    display: inline-flex; align-items: center; justify-content: center;
    flex: none;
  }

  .web-band {
    position: absolute;
    right: 0; top: 0;
    width: 30px; height: 100%;
    background: linear-gradient(to bottom, var(--orange), var(--orange-deep));
  }
  .web-band .web {
    position: absolute;
    left: 50%; bottom: 16px;
    transform-origin: left center;
    transform: translateX(6px) rotate(-90deg);
    white-space: nowrap;
    font-size: 13px;
    font-weight: 600;
    letter-spacing: 1.5px;
    color: var(--ink);
  }
</style>
</head>
<body>

  <section class="card-back" aria-label="Card back">
    <span class="back-name">TKVB</span>
  </section>

  <section class="card-front" aria-label="Card front">
    <div class="brand">
      <span class="brand-square"></span>
      <span class="brand-name">TKVB</span>
      <span class="brand-divider"></span>
      <span class="brand-tagline">Decorative<br>Concrete</span>
    </div>

    <p class="person-name"><span class="first">Howard</span> <span class="last">Pilcher</span></p>

    <div class="contact">
      <p class="address">24517-63st NW<br>Cedarvale Northland, T6W-2K8</p>
      <p class="contact-row">
        <span class="contact-icon">
          <svg width="9" height="9" viewBox="0 0 24 24"><path fill="#fff" d="M6.6 10.8a15.1 15.1 0 0 0 6.6 6.6l2.2-2.2c.3-.3.7-.4 1-.2 1.1.4 2.300.6 3.6.6.6 0 1 .4 1 1V20c0 .6-.4 1-1 1C10.6 21 3 13.4 3 4c0-.6.4-1 1-1h3.5c.6 0 1 .4 1 1 0 1.3.2 2.5.6 3.6.1.3 0 .7-.2 1z"/></svg>
        </span>
        780.555.0119
      </p>
      <p class="contact-row">
        <span class="contact-icon">
          <svg width="9" height="9" viewBox="0 0 24 24"><path fill="#fff" d="M2 5h20v14H2z"/><path fill="none" stroke="#f26a1b" stroke-width="2" d="M2 5l10 8 10-8"/></svg>
        </span>
        Howard@TkvbLtd.ca
      </p>
      <p class="contact-row">
        <span class="contact-icon"></span>
        TkvbDecorativeConcrete
      </p>
    </div>

    <div class="web-band">
      <span class="web">www.TkvbLtd.ca</span>
    </div>
  </section>

</body>
</html>
```